Willowmere Wellness Academy (Massage School) Flyer Advertisment

We are a massage therapy/holistic healing school, operating in Los Angeles for over 16 years. We need a flyer/advertisement with the aim of attracting new students and potential future massage therapists. Our vision is a 4x6 (read vertical) flyer (potentially dual sided, due to amount of copy we have). The key aesthetic terms for this project are modern, feminine, minimal, natural, fun. The design should be eye catching yet feel organic (we want an advertisement, but keep in mind we are a holistic health institution.) We would like the primary color scheme to be focused around purple and white (green or beige are secondary), and would very much like to see the use of a literal Lavender plant (or multiple) included creatively. You do not need to use all the files we provided. Mandatory is the inclusion of ALL the copy provided in the word document attached, arranged at your discretion, as well as the logo file. We have also provided a picture of our school as well as a few massage photos to possibly be used (only if applicable). Please feel free to be creative with the exact font choices and exact color choices (we only selected the options here as reference.) Thank you all so much for your time and we look forward to reviewing the designs. *Note* we have selected a 5 day duration due to urgency but may be willing to extend for the right designer (please reach out to us if need be)

Target Market(s)

Potential students to become massage therapists or holistic health professionals

Industry/Entity Type

Education

Font styles to use
Sans Serif
Script

Colors
6b449b
ffffff
fbc994
9bcb3c

Requirements
Must have
• Use of Copy attached. Use of logo. use of Lavender plant
Nice to have
• Photo our school (included). Photos of massages being done on clients (examples included)
• * Would be great if you could allow room for rounded corners on the print job* not necessary

```html
<!DOCTYPE html>
<html lang="en">
<head>
<meta charset="utf-8">
<title>Willowmere Wellness Academy – Flyer</title>
<link href="https://fonts.googleapis.com/css2?family=Questrial&family=Montserrat:wght@600;700&display=swap" rel="stylesheet">
<style>
  :root{
    --purple:#6b449b;
    --purple-dark:#4f2c7a;
    --purple-light:#9a78c4;
    --white:#ffffff;
    --ink:#2b2b2b;
    --stage:#c8c8c8;
  }
  *{margin:0;padding:0;box-sizing:border-box}
  html,body{width:1200px;height:914px;overflow:hidden}
  body{background:var(--stage);font-family:"Questrial",sans-serif;color:var(--ink);position:relative}
  .flyer{position:absolute;top:46px;width:540px;height:812px;background:var(--white);overflow:hidden}
  .flyer--front{left:36px}
  .flyer--back{left:622px}
  .flyer svg.shapes{position:absolute;inset:0;width:540px;height:812px}
  .url-top{position:absolute;top:14px;right:20px;color:var(--white);font-size:17px;letter-spacing:.3px}
  .back .url-top{left:26px;right:auto}
  .brand-seal{position:absolute;width:148px;height:148px;border-radius:50%;background:var(--white);border:5px solid var(--purple);display:flex;align-items:center;justify-content:center;text-align:center;padding:16px}
  .brand-seal span{font-family:"Questrial",sans-serif;color:var(--purple);font-size:17px;line-height:1.15}
  .headline{position:absolute;left:20px;top:322px;font-size:24px;font-weight:400;letter-spacing:.5px;color:var(--ink);line-height:1.05}
  .headline strong{display:block;font-family:"Montserrat",sans-serif;font-weight:700;color:var(--purple);font-size:23px}
  .offer-tag{position:absolute;left:0;top:386px;width:146px;height:34px;background:var(--purple);color:var(--white);font-family:"Montserrat",sans-serif;font-weight:700;font-size:18px;padding:6px 0 0 16px;border-radius:0 6px 6px 0}
  .offer-list{position:absolute;top:437px;list-style:none;font-size:17px;line-height:22.3px}
  .offer-list li{padding-left:20px;position:relative}
  .offer-list li::before{content:"";position:absolute;left:0;top:6px;width:10px;height:10px;background:var(--purple-light);border:1px solid var(--purple)}
  .offer-list--a{left:46px}
  .offer-list--b{left:326px}
  .offer-list .more{color:var(--purple)}
  .offer-list .more::before{display:none}
  .contact{position:absolute;left:0;bottom:0;width:540px;height:120px;color:var(--white)}
  .call{position:absolute;left:10px;top:49px;width:200px;text-align:center;font-family:"Montserrat",sans-serif;font-weight:700;line-height:1.1}
  .call .label{font-size:27px;display:block}
  .call .number{font-size:25px;display:block;margin-top:2px}
  .divider{position:absolute;left:230px;top:48px;width:1px;height:58px;background:rgba(255,255,255,.7)}
  .address{position:absolute;left:252px;top:50px;font-size:12.5px;line-height:15px}
  .address .line{display:flex;gap:6px;align-items:flex-start}
  .address .web{margin-top:8px;font-size:14px}
  .social{position:absolute;right:22px;top:84px;display:flex;gap:8px}
  .social i{display:block;width:20px;height:20px;border-radius:50%;background:var(--white)}
  .intro{position:absolute;right:28px;top:298px;text-align:right;color:var(--purple);font-size:23px;line-height:29px}
  .intro strong{font-family:"Montserrat",sans-serif;font-weight:700}
  .features{position:absolute;left:0;top:458px;width:540px;height:142px;background:var(--purple);list-style:none;color:var(--white);font-size:15px;padding:14px 30px 0 38px}
  .features li{position:relative;padding-left:22px;line-height:18px;margin-bottom:10px}
  .features li svg{position:absolute;left:0;top:3px}
  .licence{position:absolute;left:30px;right:30px;top:616px;text-align:center;font-size:10.5px;line-height:14px;color:var(--ink)}
</style>
</head>
<body>

<section class="flyer flyer--front front">
  <svg class="shapes" viewBox="0 0 540 812" aria-hidden="true">
    <defs>
      <linearGradient id="buildingTone" x1="0" y1="0" x2="0" y2="1">
        <stop offset="0" stop-color="#8fb3d6"/>
        <stop offset=".45" stop-color="#7d7f86"/>
        <stop offset="1" stop-color="#5f6d4f"/>
      </linearGradient>
      <linearGradient id="footFront" x1="0" y1="0" x2="1" y2="1">
        <stop offset="0" stop-color="#8360b0"/>
        <stop offset="1" stop-color="#5a3589"/>
      </linearGradient>
      <radialGradient id="skinFront" cx=".4" cy=".4" r=".7">
        <stop offset="0" stop-color="#f2c7a8"/>
        <stop offset="1" stop-color="#b87a5a"/>
      </radialGradient>
    </defs>
    <rect x="0" y="0" width="540" height="350" fill="url(#buildingTone)" role="img" aria-label="Photo of the academy building"/>
    <path d="M0 266 C150 246 310 286 540 318 L540 342 C320 306 150 272 0 288Z" fill="var(--purple)"/>
    <path d="M0 282 C150 262 320 300 540 336 L540 812 L0 812Z" fill="var(--white)"/>
    <path d="M0 672 C160 640 340 668 540 636 L540 648 C340 684 160 656 0 690Z" fill="var(--purple-light)"/>
    <path d="M0 684 C160 654 340 684 540 650 L540 812 L0 812Z" fill="url(#footFront)"/>
    <circle cx="444" cy="636" r="74" fill="url(#skinFront)" stroke="var(--purple)" stroke-width="6" role="img" aria-label="Photo of a back massage"/>
    <circle cx="110" cy="708" r="19" fill="var(--purple)" stroke="var(--white)" stroke-width="2.5"/>
    <path d="M103 699c1-1 3-1 4 0l2 4c0 1 0 2-1 3l-1 1c1 3 3 5 6 6l1-1c1-1 2-1 3-1l4 2c1 1 1 3 0 4l-2 2c-8 1-17-8-16-16z" fill="var(--white)"/>
  </svg>
  <div class="url-top">www.willowmereacademy.org</div>
  <div class="brand-seal" style="left:32px;top:158px"><span>Willowmere Wellness Academy</span></div>
  <h1 class="headline">BECOME A CERTIFIED<strong>MASSAGE THERAPIST!</strong></h1>
  <div class="offer-tag">WE OFFER</div>
  <ul class="offer-list offer-list--a">
    <li>Swedish</li><li>Deep Tissue</li><li>Myofascial Release</li><li>Chair Massage</li><li>Aromatherapy</li><li>Energy Healing</li><li>Crystal &amp; Gemstone Therapy</li><li>Shiatsu</li><li>Lymphatic</li>
  </ul>
  <ul class="offer-list offer-list--b">
    <li>Sports Massage</li><li>Pregnancy Massage</li><li>Hot Stone Massage,</li><li>Polarity Therapy</li><li class="more">and more...</li>
  </ul>
  <div class="contact">
    <div class="call"><span class="label">CALL US</span><span class="number">(818) 555-0147</span></div>
    <div class="divider"></div>
    <div class="address">
      <div class="line"><svg width="9" height="12" viewBox="0 0 9 12"><path d="M4.5 0C2 0 0 2 0 4.5 0 8 4.5 12 4.5 12S9 8 9 4.5C9 2 7 0 4.5 0zm0 6.2a1.7 1.7 0 110-3.4 1.7 1.7 0 010 3.4z" fill="#fff"/></svg><span>4120 Larkspur Ave.,<br>Los Angeles, CA 90041</span></div>
      <div class="line web"><svg width="11" height="11" viewBox="0 0 11 11"><circle cx="5.5" cy="5.5" r="5" fill="#fff"/></svg><span>www.willowmereacademy.org</span></div>
    </div>
    <div class="social"><i></i><i></i></div>
  </div>
</section>

<section class="flyer flyer--back back">
  <svg class="shapes" viewBox="0 0 540 812" aria-hidden="true">
    <defs>
      <linearGradient id="warmTone" x1="0" y1="0" x2="1" y2="1">
        <stop offset="0" stop-color="#b8561c"/>
        <stop offset=".5" stop-color="#f0a55e"/>
        <stop offset="1" stop-color="#c86a28"/>
      </linearGradient>
      <linearGradient id="footBack" x1="0" y1="0" x2="1" y2="1">
        <stop offset="0" stop-color="#8360b0"/>
        <stop offset="1" stop-color="#5a3589"/>
      </linearGradient>
      <radialGradient id="skinBack" cx=".5" cy=".4" r=".7">
        <stop offset="0" stop-color="#efc3a4"/>
        <stop offset="1" stop-color="#a86b4e"/>
      </radialGradient>
    </defs>
    <rect x="0" y="0" width="540" height="320" fill="url(#warmTone)" role="img" aria-label="Photo of a relaxing facial massage in warm light"/>
    <path d="M0 262 C170 296 360 262 540 188 L540 212 C360 286 170 322 0 288Z" fill="var(--purple)"/>
    <path d="M0 282 C170 314 360 280 540 206 L540 812 L0 812Z" fill="var(--white)"/>
    <path d="M0 672 C160 640 340 668 540 636 L540 648 C340 684 160 656 0 690Z" fill="var(--purple-light)"/>
    <path d="M0 684 C160 654 340 684 540 650 L540 812 L0 812Z" fill="url(#footBack)"/>
    <circle cx="440" cy="708" r="58" fill="url(#skinBack)" stroke="var(--purple)" stroke-width="6" role="img" aria-label="Photo of hands massaging a shoulder"/>
    <circle cx="110" cy="708" r="19" fill="var(--purple)" stroke="var(--white)" stroke-width="2.5"/>
    <path d="M103 699c1-1 3-1 4 0l2 4c0 1 0 2-1 3l-1 1c1 3 3 5 6 6l1-1c1-1 2-1 3-1l4 2c1 1 1 3 0 4l-2 2c-8 1-17-8-16-16z" fill="var(--white)"/>
  </svg>
  <div class="url-top">www.willowmereacademy.org</div>
  <div class="brand-seal" style="left:372px;top:108px"><span>Willowmere Wellness Academy</span></div>
  <p class="intro">WWA has been educating<br>students from<br>around the world<br>and all walks of life for<br><strong>over 16 years!</strong></p>
  <ul class="features">
    <li><svg width="12" height="11" viewBox="0 0 12 11"><path d="M1 6l3 3 7-8" stroke="#fff" stroke-width="2" fill="none"/></svg>Complete an affordable 300 CEU Hour Program in 15 Weeks</li>
    <li><svg width="12" height="11" viewBox="0 0 12 11"><path d="M1 6l3 3 7-8" stroke="#fff" stroke-width="2" fill="none"/></svg>2500+ Hours of Advanced Electives in various modalities</li>
    <li><svg width="12" height="11" viewBox="0 0 12 11"><path d="M1 6l3 3 7-8" stroke="#fff" stroke-width="2" fill="none"/></svg>Many classes open to the public and non-body-workers</li>
    <li><svg width="12" height="11" viewBox="0 0 12 11"><path d="M1 6l3 3 7-8" stroke="#fff" stroke-width="2" fill="none"/></svg>Study with accomplished holistic healers and seasoned health professionals</li>
  </ul>
  <p class="licence">WWA is licensed to operate by the State Office of Private Schools and fully approved by the Regional Massage Standards Council as well as the State Board of Nursing Care.</p>
  <div class="contact">
    <div class="call"><span class="label">CALL US</span><span class="number">(818) 555-0147</span></div>
    <div class="divider"></div>
    <div class="address">
      <div class="line"><svg width="9" height="12" viewBox="0 0 9 12"><path d="M4.5 0C2 0 0 2 0 4.5 0 8 4.5 12 4.5 12S9 8 9 4.5C9 2 7 0 4.5 0zm0 6.2a1.7 1.7 0 110-3.4 1.7 1.7 0 010 3.4z" fill="#fff"/></svg><span>4120 Larkspur Ave.,<br>Los Angeles, CA 90041</span></div>
      <div class="line web"><svg width="11" height="11" viewBox="0 0 11 11"><circle cx="5.5" cy="5.5" r="5" fill="#fff"/></svg><span>www.willowmereacademy.org</span></div>
    </div>
    <div class="social"><i></i><i></i></div>
  </div>
</section>

</body>
</html>
```